依頼詳細
8月にOPENいたしました。深夜に営業していることを認知していただきたいと思い依頼させていただきます。通常の個室でのマッサージだけでなくマグマ(溶岩浴)にてマッサージを受けられるのがポイント。←日本で唯一マグマ内で施術を行っております。
マグママッサージ60分受けて頂いた方→個室マッサージ30分(6,600円)サービスの掲載もお願いします。
記載項目
株式会社KORU MOVE.
VERDANT SPA
03-4829-1176
https://theverdantspa-example.jp/

温めながらほぐす究極のリラクゼーション
唯一無二の溶岩浴ボディトリートメント

料金
マグママッサージ60分¥16,200
個室マッサージ60分¥13,200
サイズ
A6
ページ数
両面
希望イメージ
シンプル 複雑
単色 カラフル
暗い 明るい
日常 高級
遊び心 厳粛
未来的 伝統的
女性的 男性的
希望する色
赤系、緑系、無彩色系、GOLD
納品ファイル
補足説明
ロゴがこちらになります。
締切日変更いたしました。
宜しくお願いします。
■ 選んだ理由

構図が良かったので選ばせて頂きました。修正やり取りも迅速に行っていただけました。ありがとうございます。

■ 提案者全員のお礼・コメント

この度はたくさんのご提案ありがとうございました。
どれも素敵で迷うものばかりでした。
また機会ありましたらよろしくお願いいたします。

```html
<!DOCTYPE html>
<html lang="ja">
<head>
<meta charset="utf-8">
<title>VERDANT SPA メニュー</title>
<link href="https://fonts.googleapis.com/css2?family=Cormorant+Garamond:wght@400;500&family=Noto+Serif+JP:wght@500;700&family=Noto+Sans+JP:wght@500;700&display=swap" rel="stylesheet">
<style>
  :root {
    --bg: #527a77;
    --line: #a7c3bf;
    --cream: #f4f0e8;
    --white: #ffffff;
    --ink: #1c1c1c;
    --band: #97b8b4;
  }
  html, body {
    margin: 0;
    padding: 0;
    overflow: hidden;
  }
  .flyer {
    position: relative;
    width: 850px;
    height: 1200px;
    background: var(--bg);
    color: var(--cream);
    overflow: hidden;
    font-family: "Noto Serif JP", serif;
  }
  .frame {
    position: absolute;
    inset: 0;
  }
  .block {
    position: absolute;
    left: 0;
    width: 100%;
    text-align: center;
    margin: 0;
  }
  .tagline {
    top: 78px;
    font-family: "Noto Sans JP", sans-serif;
    font-weight: 500;
    font-size: 22px;
    line-height: 33px;
    letter-spacing: 0.5px;
  }
  .menu-title {
    top: 198px;
    font-family: "Cormorant Garamond", serif;
    font-weight: 500;
    font-size: 80px;
    line-height: 1;
    letter-spacing: 1px;
  }
  .menu-item {
    font-weight: 700;
    font-size: 29px;
    line-height: 32px;
  }
  .menu-item.magma { top: 308px; }
  .menu-item.room { top: 403px; }
  .offer {
    top: 504px;
    font-family: "Noto Sans JP", sans-serif;
    font-weight: 700;
    font-size: 25px;
    line-height: 33px;
  }
  .offer .emph { font-size: 28px; }
  .brand-mark {
    position: absolute;
    left: 308px;
    top: 678px;
    width: 234px;
    height: 234px;
    border-radius: 50%;
    background: var(--white);
    display: flex;
    flex-direction: column;
    align-items: center;
    justify-content: center;
    color: var(--ink);
    font-family: "Cormorant Garamond", serif;
    font-weight: 500;
    text-align: center;
  }
  .brand-mark .name { font-size: 22px; letter-spacing: 1px; }
  .brand-mark .sub { font-size: 11px; margin-top: 4px; }
  .contact {
    top: 928px;
    font-family: "Cormorant Garamond", serif;
    font-weight: 500;
    font-size: 29px;
    line-height: 38px;
  }
  .contact .company { font-family: "Noto Serif JP", serif; font-size: 25px; }
  .hours {
    position: absolute;
    left: 230px;
    top: 1095px;
    width: 390px;
    height: 53px;
    background: var(--band);
    color: var(--white);
    font-family: "Noto Sans JP", sans-serif;
    font-weight: 700;
    font-size: 25px;
    line-height: 53px;
    text-align: center;
  }
</style>
</head>
<body>
<main class="flyer">
  <svg class="frame" width="850" height="1200" viewBox="0 0 850 1200" aria-hidden="true">
    <path d="M180 0 V612 A245 245 0 0 0 670 612 V0" fill="none" stroke="var(--line)" stroke-width="1.2"/>
    <path d="M180 1200 V985 A245 245 0 0 1 670 985 V1200" fill="none" stroke="var(--line)" stroke-width="1.2"/>
  </svg>

  <p class="block tagline">温めながらほぐす究極のリラクゼーション<br>唯一無二の溶岩浴ボディトリートメント</p>

  <h1 class="block menu-title">MENU</h1>

  <p class="block menu-item magma">マグママッサージ60分<br>¥16,200</p>
  <p class="block menu-item room">個室マッサージ60分<br>¥13,200</p>

  <p class="block offer">マグママッサージ60分受けて頂いた方<br>個室マッサージ30分6,600円<br><span class="emph">サービス</span></p>

  <div class="brand-mark">
    <span class="name">THE VERDANT SPA</span>
    <span class="sub">by KORU MOVE.</span>
  </div>

  <p class="block contact">
    <span class="company">株式会社 KORU MOVE.</span><br>
    VERDANT SPA<br>
    03-4829-1176<br>
    https://theverdantspa-example.jp/
  </p>

  <div class="hours">営業時間 23 時〜翌朝 6 時</div>
</main>
</body>
</html>
```